Delvin & Associates - London New Letting and Property Management Company *

Delvin & Associates LTD is a new company based in London, and works with brand new residential property in the city centre.

We are aiming to have 1000 new properties a year.

We are looking for something modern and minimalistic :
Logo ,Monogram, Paper Head and Business Card.

Target Market(s)

Internation landlords

Industry/Entity Type

Real Estate

Logo Text

Delvin & Associates

Colors

Designer to choose colors to be used in the design.

Requirements
Nice to have
• A particular monogram with "DA"
Should not have
• Little House over the logo

```html
<!DOCTYPE html>
<html lang="en">
<head>
<meta charset="utf-8">
<title>Delvin &amp; Associates LTD — Stationery</title>
<link rel="stylesheet" href="https://fonts.googleapis.com/css2?family=Exo+2:wght@400;500;600&family=Poppins:wght@400;500&display=swap">
<style>
  :root {
    --backdrop: #454759;
    --navy: #23263d;
    --paper: #f1f1f1;
    --paper-shade: #e6e6e8;
    --silver: #c9cacd;
    --ink-soft: #4a4d60;
  }
  * { margin: 0; padding: 0; box-sizing: border-box; }
  html, body { width: 884px; height: 1200px; overflow: hidden; }
  body {
    position: relative;
    background: var(--backdrop);
    font-family: "Poppins", sans-serif;
    color: var(--navy);
  }
  .sheet { position: absolute; background: var(--paper); }
  .monogram {
    font-family: "Exo 2", sans-serif;
    font-weight: 600;
    letter-spacing: 0.02em;
    line-height: 1;
    display: block;
  }

  /* Business cards */
  .card-front { left: 66px; top: 197px; width: 114px; height: 63px; }
  .card-front .brand { position: absolute; left: 6px; top: 16px; width: 52px; text-align: center; }
  .card-front .monogram { font-size: 14px; }
  .card-front .brand-name { font-family: "Exo 2", sans-serif; font-size: 4px; font-weight: 500; margin-top: 5px; white-space: nowrap; }
  .card-front .person { position: absolute; left: 57px; top: 16px; font-size: 3.6px; line-height: 1.55; color: var(--ink-soft); }
  .card-front .person .name { font-size: 4.4px; font-weight: 500; color: var(--navy); }
  .card-front .person .role { margin-bottom: 4px; }
  .card-back { left: 66px; top: 292px; width: 114px; height: 63px; display: flex; align-items: center; justify-content: center; }
  .card-back .monogram { font-size: 15px; }

  /* Letterhead */
  .letterhead { left: 236px; top: 88px; width: 266px; height: 375px; }
  .letterhead .header { position: absolute; left: 193px; top: 14px; font-size: 3.6px; line-height: 1.6; color: var(--ink-soft); }
  .letterhead .monogram { font-size: 15px; margin: 0 0 5px 12px; color: var(--navy); }
  .letterhead .brand-name { font-family: "Exo 2", sans-serif; font-size: 4px; font-weight: 500; color: var(--navy); }
  .letterhead .fold { position: absolute; left: 0; right: 0; top: 187px; height: 1px; background: var(--paper-shade); }

  /* Folder cover */
  .folder-cover { left: 562px; top: 88px; width: 272px; height: 391px; overflow: hidden; }
  .folder-cover svg { position: absolute; inset: 0; }
  .folder-cover .cover-mark { position: absolute; left: 0; right: 0; top: 178px; text-align: center; color: var(--paper); }
  .folder-cover .monogram { font-size: 60px; }
  .folder-cover .brand-name { position: absolute; left: 0; right: 0; top: 264px; text-align: center; font-family: "Exo 2", sans-serif; font-size: 15px; font-weight: 400; letter-spacing: 0.08em; color: var(--paper); white-space: nowrap; }

  /* Open folder */
  .folder-open { left: 25px; top: 535px; width: 543px; height: 392px; }
  .folder-open .spine { position: absolute; left: 271px; top: 0; bottom: 0; width: 1px; background: var(--paper-shade); }
  .folder-open svg { position: absolute; inset: 0; }

  /* Folder back */
  .folder-back { position: absolute; left: 590px; top: 535px; width: 272px; height: 392px; background: var(--navy); border: 1px solid var(--silver); display: flex; align-items: center; justify-content: center; }
  .folder-back .monogram { font-size: 60px; color: var(--paper); }

  /* Envelopes */
  .envelope { top: 982px; width: 277px; height: 139px; }
  .envelope-front { left: 66px; }
  .envelope-front .sender { position: absolute; left: 45px; top: 16px; font-size: 3.6px; line-height: 1.6; color: var(--ink-soft); }
  .envelope-front .monogram { font-size: 15px; color: var(--navy); margin: 0 0 5px 11px; }
  .envelope-front .brand-name { font-family: "Exo 2", sans-serif; font-size: 4px; font-weight: 500; color: var(--navy); }
  .envelope-front .window { position: absolute; left: 140px; top: 63px; width: 113px; height: 56px; border-radius: 6px; background: var(--paper-shade); }
  .envelope-back { left: 384px; }
  .envelope-back svg { position: absolute; inset: 0; }

  /* Pin badges */
  .badge { position: absolute; left: 702px; width: 46px; height: 46px; border-radius: 50%; }
  .badge-front { top: 982px; background: var(--navy); display: flex; align-items: center; justify-content: center; }
  .badge-front .monogram { font-size: 15px; color: var(--paper); }
  .badge-back { top: 1045px; background: var(--silver); border: 4px solid var(--paper-shade); }
</style>
</head>
<body>

  <section class="sheet card-front" aria-label="Business card, front">
    <div class="brand">
      <span class="monogram">DA</span>
      <div class="brand-name">DELVIN &amp; ASSOCIATES LTD</div>
    </div>
    <div class="person">
      <div class="name">Oskar Lindqvist</div>
      <div class="role">property consultant</div>
      <div>020 7946 0321</div>
      <div>hello@delvinassociates.co.uk</div>
      <div>www.delvinassociates.co.uk</div>
    </div>
  </section>

  <section class="sheet card-back" aria-label="Business card, back">
    <span class="monogram">DA</span>
  </section>

  <section class="sheet letterhead" aria-label="Letterhead">
    <div class="header">
      <span class="monogram">DA</span>
      <div class="brand-name">DELVIN &amp; ASSOCIATES LTD</div>
      <div>020 7946 0321</div>
      <div>hello@delvinassociates.co.uk</div>
      <div>www.delvinassociates.co.uk</div>
    </div>
    <div class="fold"></div>
  </section>

  <section class="sheet folder-cover" aria-label="Presentation folder, cover">
    <svg viewBox="0 0 236 391" width="272" height="391" preserveAspectRatio="none" aria-hidden="true">
      <path fill="var(--navy)" d="M0,40 C30,20 70,-5 110,0 C140,4 150,40 180,55 C205,68 236,80 236,90 L236,160 C215,185 195,205 205,240 C215,270 236,285 236,300 L236,391 L180,391 C160,360 130,330 100,335 C60,342 30,380 0,391 L0,215 C20,190 28,160 10,130 C4,118 0,110 0,100 Z"/>
    </svg>
    <div class="cover-mark"><span class="monogram">DA</span></div>
    <div class="brand-name">DELVIN &amp; ASSOCIATES LTD</div>
  </section>

  <section class="sheet folder-open" aria-label="Presentation folder, open">
    <div class="spine"></div>
    <svg viewBox="0 0 543 392" width="543" height="392" aria-hidden="true">
      <path fill="var(--navy)" d="M490,0 H543 V392 H271 L287,332 Q290,322 300,322 H463 V40 Q463,8 490,0 Z"/>
    </svg>
  </section>

  <section class="folder-back" aria-label="Presentation folder, back">
    <span class="monogram">DA</span>
  </section>

  <section class="sheet envelope envelope-front" aria-label="Envelope, front">
    <div class="sender">
      <span class="monogram">DA</span>
      <div class="brand-name">DELVIN &amp; ASSOCIATES LTD</div>
      <div>020 7946 0321</div>
      <div>hello@delvinassociates.co.uk</div>
      <div>www.delvinassociates.co.uk</div>
    </div>
    <div class="window"></div>
  </section>

  <section class="sheet envelope envelope-back" aria-label="Envelope, back">
    <svg viewBox="0 0 277 139" width="277" height="139" aria-hidden="true">
      <path fill="none" stroke="var(--paper-shade)" stroke-width="1" d="M0,14 H120 Q138,14 138,30 Q138,14 156,14 H277"/>
    </svg>
  </section>

  <div class="badge badge-front"><span class="monogram">DA</span></div>
  <div class="badge badge-back"></div>

</body>
</html>
```